Modern Lawfirm Business Card Design

We're looking for a business card to incorporate the newly created logo we had made.

Ideally looking for a law firm business card demonstrating, modern, minimalist, strong/bold design.

I'm open to any design honestly, but nothing "flashy".

Target Market(s)

Immigration law, family immigration, humanitarian, general legal

Industry/Entity Type

Law Firm

Contact Information for Business Card

Please use dummy information, name, street address, city, state, phone number, email, website.

Font styles to use
Serif
Sans Serif

Requirements
Must have
• Please use dummy information, name, street address, city, state, phone number, email, website.

```html
<!DOCTYPE html>
<html lang="en">
<head>
<meta charset="utf-8">
<title>Valcourt Immigration Law – Business Card</title>
<link href="https://fonts.googleapis.com/css2?family=Cinzel:wght@500&family=Cabin:wght@400;600&display=swap" rel="stylesheet">
<style>
  :root {
    --page: #e9e9e9;
    --ink-dark: #2b2b2b;
    --ink-darker: #1c1c1c;
    --band-light: #f1f1f1;
    --text-light: #ffffff;
    --text-dark: #262626;
    --icon-bg: #2f2f2f;
  }
  * { margin: 0; padding: 0; box-sizing: border-box; }
  html, body {
    width: 1200px; height: 1000px; overflow: hidden;
    background: var(--page);
    font-family: "Cabin", sans-serif;
  }
  .stage {
    position: relative; width: 1200px; height: 1000px;
    display: flex; align-items: center; justify-content: center; gap: 30px;
  }
  .card {
    position: relative; width: 540px; height: 310px; overflow: hidden;
    box-shadow: 0 6px 18px rgba(0,0,0,.18);
  }
  .card--back {
    background: linear-gradient(160deg, var(--ink-dark), var(--ink-darker));
    display: flex; align-items: center; justify-content: center;
  }
  .brand { display: flex; align-items: center; gap: 10px; color: var(--text-light); }
  .brand__mark { width: 12px; height: 12px; background: var(--text-light); }
  .brand__text { display: flex; flex-direction: column; }
  .brand__name {
    font-family: "Cinzel", serif; font-weight: 500; font-size: 30px;
    letter-spacing: 2px; line-height: 1;
  }
  .brand__tag {
    font-family: "Cinzel", serif; font-weight: 500; font-size: 9px;
    letter-spacing: 4px; margin-top: 4px; text-transform: uppercase;
  }
  .card--front { background: var(--ink-dark); }
  .front__top { position: absolute; inset: 0 0 auto 0; height: 168px; background: linear-gradient(160deg, var(--ink-dark), var(--ink-darker)); }
  .front__brand { position: absolute; top: 28px; right: 30px; }
  .front__brand .brand__name { font-size: 26px; }
  .person { position: absolute; left: 30px; bottom: 14px; color: var(--text-light); }
  .person__name { font-family: "Cinzel", serif; font-weight: 500; font-size: 26px; letter-spacing: 1.5px; }
  .person__title { font-weight: 600; font-size: 14px; margin-top: 4px; }
  .front__band {
    position: absolute; top: 168px; left: 0; right: 0; height: 100px;
    background: var(--band-light); color: var(--text-dark);
    display: flex; justify-content: space-between; padding: 14px 30px;
  }
  .front__base { position: absolute; top: 268px; left: 0; right: 0; bottom: 0; background: var(--ink-darker); }
  .contact-list { list-style: none; display: flex; flex-direction: column; gap: 7px; }
  .contact-list li { display: flex; align-items: center; gap: 8px; font-size: 13px; }
  .icon { width: 18px; height: 18px; flex: none; }
</style>
</head>
<body>
<main class="stage">
  <section class="card card--back" aria-label="Card back">
    <div class="brand">
      <span class="brand__mark"></span>
      <div class="brand__text">
        <span class="brand__name">VALCOURT</span>
        <span class="brand__tag">Immigration Law</span>
      </div>
    </div>
  </section>

  <section class="card card--front" aria-label="Card front">
    <div class="front__top">
      <div class="brand front__brand">
        <span class="brand__mark"></span>
        <div class="brand__text">
          <span class="brand__name">VALCOURT</span>
          <span class="brand__tag">Immigration Law</span>
        </div>
      </div>
      <div class="person">
        <h1 class="person__name">MARA ELLISON</h1>
        <p class="person__title">Attorney &amp; Counselor at law</p>
      </div>
    </div>

    <div class="front__band">
      <ul class="contact-list">
        <li>
          <svg class="icon" viewBox="0 0 18 18"><circle cx="9" cy="9" r="9" fill="var(--icon-bg)"/><path d="M9 4a3 3 0 0 0-3 3c0 2.3 3 6 3 6s3-3.7 3-6a3 3 0 0 0-3-3z" fill="#fff"/><circle cx="9" cy="7" r="1.1" fill="var(--icon-bg)"/></svg>
          1418 Harlow Ave, Brookmere, PA, 18050
        </li>
        <li>
          <svg class="icon" viewBox="0 0 18 18"><circle cx="9" cy="9" r="9" fill="var(--icon-bg)"/><rect x="4.5" y="6" width="9" height="6.5" fill="none" stroke="#fff" stroke-width="1.1"/><path d="M4.5 6 9 9.6 13.5 6" fill="none" stroke="#fff" stroke-width="1.1"/></svg>
          www.ellisonlegal.com
        </li>
        <li>
          <svg class="icon" viewBox="0 0 18 18"><circle cx="9" cy="9" r="9" fill="var(--icon-bg)"/><path d="M4.5 9 9 5l4.5 4M6 8.2V13h6V8.2" fill="none" stroke="#fff" stroke-width="1.2"/></svg>
          mara@ellisonlegal.com
        </li>
      </ul>
      <ul class="contact-list">
        <li>
          <svg class="icon" viewBox="0 0 18 18"><circle cx="9" cy="9" r="9" fill="var(--icon-bg)"/><path d="M6 4.8l1.6 2-1 1.1a6 6 0 0 0 3.5 3.5l1.1-1 2 1.6-1 1.5c-3.5 0-7.2-3.7-7.2-7.2z" fill="#fff"/></svg>
          555-201-3846
        </li>
        <li>
          <svg class="icon" viewBox="0 0 18 18"><circle cx="9" cy="9" r="9" fill="var(--icon-bg)"/><rect x="6.3" y="4.3" width="5.4" height="9.4" rx="1" fill="none" stroke="#fff" stroke-width="1.1"/><circle cx="9" cy="12" r=".6" fill="#fff"/></svg>
          555-310-7729
        </li>
        <li>
          <svg class="icon" viewBox="0 0 18 18"><circle cx="9" cy="9" r="9" fill="var(--icon-bg)"/><rect x="6.5" y="4.5" width="5" height="3" fill="#fff"/><rect x="4.5" y="7.5" width="9" height="4" rx=".8" fill="#fff"/><rect x="6.5" y="10.5" width="5" height="3" fill="#fff" stroke="var(--icon-bg)" stroke-width=".6"/></svg>
          555-418-2057
        </li>
      </ul>
    </div>
    <div class="front__base"></div>
  </section>
</main>
</body>
</html>
```